Courier Business needs a Business Card Design !!!

My new company needs a business card design. Our company name is Maple Dart Courier & Delivery Services. We will be servicing residential , government and business clients in the City of Yellowknife, Northwest Territories, Canada. I would like the following information included on the card: Name- Calvin Oxley. Title- Owner. Company- Maple Dart Courier & Delivery Services. Address- PO Box 5918 , Yellowknife , NWT, X0E 4K3. Phone- 867-555-0193. Email- mapledartdelivery@postfern.example. Facebook- www.socialpage.example/mapledartdelivery. I would like my double sided card to be the standard size of 84mm x 55mm. No borders. Use CMYK mode.1039x 697 pixels at least. I would like my logo to take up at least one quarter of the area of one side of the card. Text should be at least 8 point with perhaps my name being 10 point and my company name being 12-15 point . It should have clear readable font. Please use one or two bold colors. I am trying to attract the business community so a professional look might be best. My tag line is " On Time Every Time ". Nice safe margins please. We will be providing fast, reliable and professional delivery of envelopes and small packages within the City of Yellowknife. We offer 100% satisfaction or a complete refund. I have included a file of our logo. I like black, blue and red but am willing to look at what you feel would work best. I do not really like white as a background color.

Target Market(s)

Professionals , business owners. 30-50 years old

Industry/Entity Type

Residential

Contact Information for Business Card

As noted in brief

Font styles to use
Serif
Sans Serif

Colors
000000
0255a3
f04a50

Requirements
Must have
• My contact info. My logo
Nice to have
• Simple elegant design but still catches the eye
Should not have
• White background color

```html
<!DOCTYPE html>
<html lang="en">
<head>
<meta charset="utf-8">
<title>Maple Dart Courier &amp; Delivery Services – Business Card</title>
<link rel="stylesheet" href="https://fonts.googleapis.com/css2?family=Cabin:wght@400;600&display=swap">
<style>
  :root {
    --backdrop: #1c1c1c;
    --card-white: #ffffff;
    --crimson: #dc2249;
    --ink: #111111;
    --paper-text: #ffffff;
    --tag-grey: #555555;
  }
  * { margin: 0; padding: 0; box-sizing: border-box; }
  html, body {
    width: 1200px; height: 900px; overflow: hidden;
    background: var(--backdrop);
    font-family: "Cabin", "Gill Sans", sans-serif;
  }
  .canvas { position: relative; width: 1200px; height: 900px; }

  .card {
    position: absolute; left: 98px; top: 128px;
    width: 992px; height: 649px;
    border-radius: 42px; overflow: hidden;
    background: var(--card-white);
  }
  .card__band {
    position: absolute; left: 0; top: 264px; width: 100%; bottom: 0;
    background: var(--crimson);
  }

  /* brand block */
  .brand { position: absolute; left: 40px; top: 70px; width: 440px; }
  .brand__row { display: flex; align-items: center; gap: 16px; }
  .brand__dot {
    flex: none; width: 22px; height: 22px; border-radius: 50%;
    background: var(--crimson);
  }
  .brand__name {
    color: var(--crimson); font-weight: 600;
    font-size: 46px; line-height: 1.05; letter-spacing: 0.5px;
  }
  .brand__name span { display: block; font-size: 27px; letter-spacing: 0.3px; }
  .brand__tagline {
    margin-top: 14px; margin-left: 38px;
    font-size: 15px; letter-spacing: 4px; text-transform: uppercase;
    color: var(--tag-grey);
  }

  /* name block */
  .holder { position: absolute; right: 38px; top: 112px; text-align: right; }
  .holder__name { color: var(--crimson); font-size: 42px; font-weight: 400; line-height: 1; }
  .holder__title { color: var(--crimson); font-size: 21px; margin-top: 6px; }
  .holder__tab {
    position: absolute; right: 0; top: 109px; width: 30px; height: 74px;
    background: var(--crimson);
  }

  /* contact list */
  .contact-tab {
    position: absolute; left: 0; top: 315px; width: 35px; height: 165px;
    background: var(--ink);
  }
  .contacts { position: absolute; left: 46px; top: 329px; list-style: none; }
  .contacts li {
    display: flex; align-items: center; gap: 10px;
    height: 32px; margin-bottom: 24px;
    color: var(--ink); font-size: 25px;
  }
  .contacts svg { flex: none; }

  /* address */
  .address {
    position: absolute; right: 43px; top: 440px;
    text-align: right; font-style: normal;
    color: var(--paper-text); font-size: 25px; line-height: 44px;
  }
  .address-tab {
    position: absolute; right: 0; top: 444px; width: 30px; height: 116px;
    background: var(--card-white);
  }
</style>
</head>
<body>
<div class="canvas">
  <section class="card" aria-label="Business card">
    <div class="card__band"></div>

    <div class="brand">
      <div class="brand__row">
        <div class="brand__dot"></div>
        <div class="brand__name">Maple Dart<span>Courier &amp; Delivery Services</span></div>
      </div>
      <p class="brand__tagline">On Time Every Time</p>
    </div>

    <div class="holder">
      <h1 class="holder__name">Calvin Oxley</h1>
      <p class="holder__title">Owner</p>
    </div>
    <div class="holder__tab"></div>

    <div class="contact-tab"></div>
    <ul class="contacts">
      <li>
        <svg width="32" height="32" viewBox="0 0 32 32" aria-hidden="true">
          <circle cx="16" cy="16" r="16" fill="#111"/>
          <path d="M11 8c1 0 2 2.5 2.5 4 .3 1-1.3 1.8-1 2.8.7 2 2.5 3.8 4.5 4.6 1 .3 1.8-1.3 2.8-1 1.5.5 4 1.5 4 2.5 0 1.5-2 3.2-3.5 3.2C14 24 8 18 8 11.5 8 10 9.5 8 11 8z" fill="#dc2249"/>
        </svg>
        867-555-0193
      </li>
      <li>
        <svg width="32" height="32" viewBox="0 0 32 32" aria-hidden="true">
          <circle cx="16" cy="16" r="16" fill="#111"/>
          <rect x="8" y="10.5" width="16" height="11" rx="1" fill="none" stroke="#dc2249" stroke-width="1.8"/>
          <path d="M8.5 11.5 16 17l7.5-5.5" fill="none" stroke="#dc2249" stroke-width="1.8"/>
        </svg>
        mapledartdelivery@postfern.example
      </li>
      <li>
        <svg width="32" height="32" viewBox="0 0 32 32" aria-hidden="true">
          <circle cx="16" cy="16" r="16" fill="#111"/>
          <circle cx="16" cy="16" r="9" fill="none" stroke="#dc2249" stroke-width="1.6"/>
          <ellipse cx="16" cy="16" rx="4" ry="9" fill="none" stroke="#dc2249" stroke-width="1.4"/>
          <path d="M7 16h18" stroke="#dc2249" stroke-width="1.4"/>
        </svg>
        www.socialpage.example/mapledartdelivery
      </li>
    </ul>

    <address class="address">
      PO Box 5918<br>
      Yellowknife, NWT,<br>
      X0E 4K3.
    </address>
    <div class="address-tab"></div>
  </section>
</div>
</body>
</html>
```